Plover Freightworks Business Card Design

We are a trucking and warehousing company. We run freight in the US manly from the Pacific NW to TX and back up the the PNW. We also do warehousing where we store, move, and distribute freight. Looking for a clean and modern design of business card. We would like to look rich and elegant. Attached is our logo.

Industry/Entity Type

Trucking Company

Contact Information for Business Card

Looking for a clean and modern design of business card. We would like to look rich and elegant.

Font styles to use
Sans Serif

Colors

Designer to choose colors to be used in the design.

Requirements
Must have
• logo but it should not dominate the card
Should not have
• logo should not dominate the card

```html
<!DOCTYPE html>
<html lang="en">
<head>
<meta charset="utf-8">
<title>Plover Freightworks Business Card</title>
<link rel="stylesheet" href="https://fonts.googleapis.com/css2?family=Open+Sans:wght@400;600&display=swap">
<style>
  :root {
    --stage: #1c1c1c;
    --card: #1b1b1c;
    --card-edge: #2a2a2b;
    --ink: #f2f2f2;
    --ink-soft: #d6d6d6;
    --blue: #1a7bd0;
    --orange: #f29a1c;
    --rule: #3a3a3c;
  }
  * { box-sizing: border-box; margin: 0; padding: 0; }
  html, body { width: 1200px; height: 900px; overflow: hidden; }
  body {
    background: var(--stage);
    font-family: "Open Sans", sans-serif;
    color: var(--ink);
    display: flex;
    flex-direction: column;
    align-items: center;
    justify-content: center;
    gap: 44px;
  }
  .card {
    width: 580px;
    height: 330px;
    border-radius: 22px;
    background: linear-gradient(150deg, #222224 0%, var(--card) 55%, #161617 100%);
    border: 1px solid var(--card-edge);
    box-shadow: 0 18px 40px rgba(0,0,0,.55);
    position: relative;
    overflow: hidden;
  }

  /* wordmark */
  .wordmark { display: flex; align-items: center; gap: 14px; }
  .wordmark-dot {
    width: 44px; height: 44px; border-radius: 50%;
    background: var(--blue);
    flex: none;
  }
  .wordmark-name {
    font-weight: 600;
    color: var(--ink);
    text-transform: uppercase;
    line-height: 1.05;
    letter-spacing: 1px;
  }

  /* front */
  .card-front {
    display: flex; flex-direction: column; align-items: center; justify-content: center; gap: 54px;
  }
  .card-front .wordmark-name { font-size: 30px; }
  .card-front .web {
    color: var(--orange);
    font-weight: 600;
    font-size: 17px;
    letter-spacing: 2px;
    text-transform: uppercase;
  }

  /* back */
  .card-back .wordmark {
    position: absolute; top: 52px; right: 44px;
  }
  .card-back .wordmark-name { font-size: 24px; }
  .card-back .divider {
    position: absolute; top: 142px; left: 44px; right: 44px;
    height: 1px; background: var(--rule);
  }
  .person { position: absolute; left: 44px; top: 166px; }
  .person-name { font-size: 21px; letter-spacing: 1px; text-transform: uppercase; color: var(--blue); }
  .person-name .surname { color: var(--orange); }
  .person-role { font-size: 15px; color: var(--ink-soft); margin-top: 2px; }
  .contact-list { list-style: none; margin-top: 12px; }
  .contact-list li { display: flex; align-items: center; gap: 10px; font-size: 15px; color: var(--ink-soft); line-height: 24px; }
  .contact-list svg { width: 13px; height: 13px; fill: var(--blue); flex: none; }
  .address {
    position: absolute; right: 44px; top: 172px;
    text-align: right; font-size: 15px; color: var(--ink-soft); line-height: 22px; font-style: normal;
  }
</style>
</head>
<body>

  <section class="card card-front" aria-label="Card front">
    <div class="wordmark">
      <span class="wordmark-dot"></span>
      <span class="wordmark-name">Plover Freightworks, LLC</span>
    </div>
    <p class="web">www.ploverfreight.com</p>
  </section>

  <section class="card card-back" aria-label="Card back">
    <div class="wordmark">
      <span class="wordmark-dot"></span>
      <span class="wordmark-name">Plover Freightworks, LLC</span>
    </div>
    <div class="divider"></div>

    <div class="person">
      <p class="person-name">Marcus <span class="surname">Dalton</span></p>
      <p class="person-role">Managing Director</p>
      <ul class="contact-list">
        <li>
          <svg viewBox="0 0 16 16" aria-hidden="true"><path d="M2 5c0-2 2-3 6-3s6 1 6 3v1h-3V5H5v1H2z M3 8h10l1 6H2z"/></svg>
          041-555 208 316
        </li>
        <li>
          <svg viewBox="0 0 16 16" aria-hidden="true"><path d="M4 1h8a1 1 0 0 1 1 1v12a1 1 0 0 1-1 1H4a1 1 0 0 1-1-1V2a1 1 0 0 1 1-1zm1 2v9h6V3z"/></svg>
          041-555 208 317
        </li>
        <li>
          <svg viewBox="0 0 16 16" aria-hidden="true"><path d="M1 3h14v10H1z M1 3l7 6 7-6" stroke="#1b1b1c" stroke-width="1.2"/></svg>
          info@ploverfreight.com
        </li>
        <li>
          <svg viewBox="0 0 16 16" aria-hidden="true"><circle cx="8" cy="8" r="7"/></svg>
          www.ploverfreight.com
        </li>
      </ul>
    </div>

    <address class="address">
      12345, Address Goes Here<br>
      Country Name, 123456
    </address>
  </section>

</body>
</html>
```